DL Flyer for garden consultants. I will supply text and logo

To design an eye catching but simple, uncluttered flyer for letter box distribution. The text and logo are provided.

```html
<!DOCTYPE html>
<html lang="en">
<head>
<meta charset="utf-8">
<title>Verdell Garden Consultants – DL Flyer</title>
<link rel="stylesheet" href="https://fonts.googleapis.com/css2?family=Lato:wght@400;700&family=Saira+Extra+Condensed:wght@600;700&display=swap">
<style>
  :root {
    --backdrop: #3a3b3d;
    --leaf-green: #3db54a;
    --forest-green: #0f5a2b;
    --lime: #c9dc2b;
    --paper: #ffffff;
    --sky-blue: #7a9fd8;
    --daffodil: #b9c43a;
  }
  * { margin: 0; padding: 0; box-sizing: border-box; }
  html, body { width: 1200px; height: 865px; overflow: hidden; }
  body {
    background: var(--backdrop);
    font-family: "Lato", Arial, sans-serif;
    position: relative;
  }
  .flyer {
    position: absolute;
    left: 405px;
    top: 20px;
    width: 390px;
    height: 825px;
    background: var(--leaf-green);
    overflow: hidden;
  }
  .flyer-shapes { position: absolute; left: 0; top: 0; }
  .display-type {
    font-family: "Saira Extra Condensed", "Arial Narrow", sans-serif;
    font-weight: 700;
    text-transform: uppercase;
  }
  .headline-lead { fill: var(--lime); font-size: 44px; }
  .headline-follow { fill: var(--forest-green); font-size: 28px; }
  .web-address { fill: var(--paper); font-size: 30px; font-weight: 600; }
  .brand {
    position: absolute;
    right: 26px;
    top: 70px;
    display: flex;
    align-items: center;
    gap: 10px;
  }
  .brand-dot {
    width: 30px; height: 30px;
    border-radius: 50%;
    background: var(--leaf-green);
    flex: none;
  }
  .brand-name {
    font-family: "Lato", Arial, sans-serif;
    font-weight: 700;
    color: var(--leaf-green);
    font-size: 15px;
    line-height: 1.1;
    text-transform: uppercase;
    white-space: nowrap;
  }
  .photo {
    position: absolute;
    border-radius: 50%;
    border: 7px solid var(--lime);
    box-shadow: 0 0 0 3px var(--paper);
  }
  .photo-fern {
    left: 16px; top: 196px; width: 176px; height: 176px;
    background: radial-gradient(circle at 55% 45%, #3f6b3a 0%, #5c8a5a 25%, var(--sky-blue) 60%, #5f86c7 100%);
  }
  .photo-daffodils {
    left: 214px; top: 292px; width: 150px; height: 150px;
    background: radial-gradient(circle at 45% 55%, #e3e06a 0%, var(--daffodil) 35%, #3f6b2a 75%, #2a4a1e 100%);
  }
  .services {
    position: absolute;
    left: 22px;
    right: 18px;
    top: 392px;
    color: var(--paper);
  }
  .services-title {
    font-family: "Saira Extra Condensed", "Arial Narrow", sans-serif;
    font-weight: 700;
    font-size: 24px;
    color: var(--forest-green);
    text-transform: uppercase;
    line-height: 1;
    margin-bottom: 28px;
    white-space: nowrap;
  }
  .services-list { list-style: none; }
  .services-list li {
    position: relative;
    padding-left: 16px;
    font-size: 14px;
    line-height: 17px;
    margin-bottom: 4px;
  }
  .services-list li::before {
    content: "";
    position: absolute;
    left: 0; top: 6px;
    width: 6px; height: 6px;
    border-radius: 50%;
    background: var(--forest-green);
  }
</style>
</head>
<body>
  <main class="flyer">
    <svg class="flyer-shapes" width="390" height="825" viewBox="0 0 390 825">
      <path d="M0 52 Q190 20 390 70 L390 450 Q220 350 0 350 Z" fill="var(--paper)"/>
      <path d="M0 52 Q190 20 390 70" fill="none" stroke="var(--lime)" stroke-width="4"/>
      <path d="M0 350 Q220 350 390 450" fill="none" stroke="var(--lime)" stroke-width="4"/>
      <path d="M0 712 Q200 690 390 735 L390 825 L0 825 Z" fill="var(--forest-green)"/>
      <path d="M0 706 Q200 684 390 729" fill="none" stroke="var(--lime)" stroke-width="4"/>
      <text class="display-type headline-lead" x="20" y="150" textLength="352" lengthAdjust="spacingAndGlyphs">Have you been thinking</text>
      <text class="display-type headline-follow" x="20" y="180" textLength="352" lengthAdjust="spacingAndGlyphs">About your garden lately? Well…</text>
      <text class="display-type web-address" x="25" y="785" textLength="340" lengthAdjust="spacingAndGlyphs">www.verdellgarden.com.au</text>
    </svg>

    <div class="brand">
      <span class="brand-dot"></span>
      <span class="brand-name">Verdell<br>Garden Consultants</span>
    </div>

    <div class="photo photo-fern" role="img" aria-label="Photo looking up into the fronds of a tree fern against blue sky"></div>
    <div class="photo photo-daffodils" role="img" aria-label="Photo of yellow daffodils in bloom"></div>

    <section class="services">
      <h2 class="services-title">Our services:</h2>
      <ul class="services-list">
        <li>Appraisal of the existing plant palette and condition</li>
        <li>Analysis of the soil structure and pH</li>
        <li>Review of the hardscape from the viewpoint of design and amenity</li>
        <li>Isolating the important site features and</li>
        <li>The key design elements within your property</li>
        <li>Recommendations and possibilities to help realise the dream</li>
      </ul>
    </section>
  </main>
</body>
</html>
```